We need a new brochure design for our dental clinic, Briar Dental. We have attached the information we want printed and photos to include.

Industry/Entity Type

Dental

```html
<!DOCTYPE html>
<html lang="en">
<head>
<meta charset="utf-8">
<title>Briar Dental – Brochure</title>
<link href="https://fonts.googleapis.com/css2?family=Didact+Gothic&display=swap" rel="stylesheet">
<style>
  :root {
    --blue-deep: #0b4c9c;
    --blue-mid: #1466bb;
    --blue-light: #2a8ad6;
    --green: #8cc63f;
    --lime: #c5de2f;
    --white: #ffffff;
    --clinic-tone-a: #d9d4cc;
    --clinic-tone-b: #b83a32;
    --xray-tone-a: #0c0c0e;
    --xray-tone-b: #c8731c;
    --tooth-tone-a: #b9a493;
    --tooth-tone-b: #6e4a3c;
  }
  * { margin: 0; padding: 0; box-sizing: border-box; }
  html, body { width: 1200px; height: 848px; overflow: hidden; background: var(--white); }
  .brochure {
    position: relative;
    width: 1200px;
    height: 848px;
    overflow: hidden;
    font-family: "Didact Gothic", "Century Gothic", sans-serif;
    color: var(--white);
    background: var(--white);
  }
  .photo { position: absolute; }
  .photo--clinic {
    left: 0; top: 0; width: 408px; height: 340px;
    background: linear-gradient(135deg, var(--clinic-tone-a) 0%, #c9c2b6 45%, var(--clinic-tone-b) 75%, #7a2a25 100%);
  }
  .photo--xray {
    left: 408px; top: 0; width: 420px; height: 360px;
    background: radial-gradient(ellipse at 45% 45%, var(--xray-tone-b) 0%, #6b3a12 30%, var(--xray-tone-a) 65%);
  }
  .photo--tooth {
    left: 828px; top: 0; width: 372px; height: 360px;
    background: radial-gradient(ellipse at 55% 45%, #d8c8b8 0%, var(--tooth-tone-a) 35%, var(--tooth-tone-b) 80%);
  }
  .waves { position: absolute; left: 0; top: 0; width: 1200px; height: 848px; }
  .panel-text {
    position: absolute;
    font-size: 17.4px;
    line-height: 22.2px;
    letter-spacing: 0.1px;
  }
  .panel-text p + p { margin-top: 22px; }
  .panel-text--left { left: 14px; top: 378px; width: 392px; }
  .panel-text--middle { left: 412px; top: 348px; width: 385px; }
  .panel-text--right { left: 824px; top: 382px; width: 360px; }
  .brand {
    position: absolute;
    left: 862px; top: 718px;
    display: flex; align-items: center; gap: 26px;
  }
  .brand__mark { width: 68px; height: 68px; background: var(--white); }
  .brand__name {
    font-size: 37px; line-height: 40px; letter-spacing: 1px;
    text-transform: uppercase; color: var(--white); text-align: center;
  }
</style>
</head>
<body>
<main class="brochure">
  <div class="photo photo--clinic" role="img" aria-label="Photo of a dental treatment room with red patient chairs and a wall monitor"></div>
  <div class="photo photo--xray" role="img" aria-label="X-ray style side view of a head showing the jaw and teeth"></div>
  <div class="photo photo--tooth" role="img" aria-label="Close-up photo of a molar with a mercury filling and cracks, marked by an arrow"></div>

  <svg class="waves" viewBox="0 0 1200 848" aria-hidden="true">
    <defs>
      <linearGradient id="panelBlue" x1="0" y1="0" x2="1" y2="1">
        <stop offset="0" stop-color="var(--blue-deep)"/>
        <stop offset="0.55" stop-color="var(--blue-mid)"/>
        <stop offset="1" stop-color="var(--blue-light)"/>
      </linearGradient>
      <linearGradient id="swooshGreen" x1="0" y1="0" x2="1" y2="0">
        <stop offset="0" stop-color="var(--green)"/>
        <stop offset="1" stop-color="var(--lime)"/>
      </linearGradient>
    </defs>
    <!-- left frame arc of the tooth panel -->
    <path d="M828,0 C900,80 905,250 860,360 L828,360 Z" fill="var(--blue-mid)"/>
    <path d="M850,0 C915,90 915,250 872,360 L860,360 C905,250 900,90 838,0 Z" fill="url(#swooshGreen)"/>
    <!-- top-right swoosh -->
    <path d="M1040,0 C1140,20 1200,60 1200,60 L1200,0 Z" fill="url(#swooshGreen)"/>
    <!-- green band -->
    <path d="M0,316 C160,270 320,242 450,244 C620,246 760,288 862,336 C970,318 1090,240 1200,110 L1200,848 L0,848 Z" fill="url(#swooshGreen)"/>
    <!-- white band -->
    <path d="M0,328 C160,284 320,256 450,257 C620,259 760,300 862,348 C970,332 1090,256 1200,128 L1200,848 L0,848 Z" fill="var(--white)"/>
    <!-- blue panel body -->
    <path d="M0,338 C160,296 320,268 450,268 C620,270 760,310 862,358 C970,344 1090,270 1200,142 L1200,848 L0,848 Z" fill="url(#panelBlue)"/>
  </svg>

  <section class="panel-text panel-text--left">
    <p>Your smile may be saying more about you than you realise.&nbsp; Studies have shown that an attractive&nbsp; smile gives the perception of an individual to be successful, healthy and sociable.&nbsp; The same studies show that an unattractive smile gives the perception of an individual to be less successful,&nbsp; having a dull social life and even being less trustworthy. Ofcourse these are just perceptions and often can be changed after getting to know a person in due time. However there may be instances where one does not get the benefit of time to make a lasting impression.&nbsp; Studies indicate that lasting impressions are made within the first three seconds of seeing someone.&nbsp; Cosmetic dentistry can greatly improve the attractiveness of a smile and help create a great first impression!</p>
  </section>

  <section class="panel-text panel-text--middle">
    <p>90% of dental diseases have little or no symptoms till advanced stages. When dental diseases reach an advanced stage the pain can be very sudden, intense and often accompanied by facial swelling. At this stage complex dental treatment would be needed to treat the tooth.</p>
    <p>Dental problems need not only be related to the teeth and gums. The health of the mouth depends on the harmonious inter-relationship between the teeth, muscles of the jaw and the temporomandibular joint. When an unhealthy relationship exists between these structures an individual can experience excessive tooth wear, shaky loose teeth, cracks or fractures, ear congestion, headaches, facial pain and postural problems.</p>
  </section>

  <section class="panel-text panel-text--right">
    <p>The photo above shows a tooth with a mercury filling which has, over time, caused cracks to form along the tooth. These cracks are usually painless until they reach the nerve of the tooth. At this time the cracks can split the tooth and the pain can be sudden and excruciating.</p>
    <p>Our Halden Treatment Centre provides excellent comfort for our patients with its advanced thermo upholstery and lumbar support.</p>
  </section>

  <div class="brand">
    <span class="brand__mark"></span>
    <span class="brand__name">Briar<br>Dental</span>
  </div>
</main>
</body>
</html>
```